KORVELLA Corporate Business Card

Modern business card design for company which focuses in the areas of Staffing, IT Consulting & Data Services. Please note: We are no longer using the IT subscript on the logo. All designs should have IT subscript removed.
Website: www.korvellait.example

```html
<!DOCTYPE html>
<html lang="en">
<head>
<meta charset="utf-8">
<title>KORVELLA Business Card</title>
<link rel="stylesheet" href="https://fonts.googleapis.com/css2?family=Montserrat:wght@500;600;700&family=Roboto:wght@400;500&display=swap">
<style>
  :root {
    --stage: #3a3a3a;
    --brand-blue: #1e90d6;
    --brand-deep: #0d5c9c;
    --brand-navy: #0a4478;
    --ink-blue: #1f5f96;
    --paper: #ffffff;
    --faint: #e6ecf5;
  }
  * { box-sizing: border-box; margin: 0; padding: 0; }
  html, body { width: 1200px; height: 901px; overflow: hidden; }
  body {
    background: var(--stage);
    display: flex; align-items: center; justify-content: center; gap: 40px;
    font-family: "Roboto", Arial, sans-serif;
  }
  .card {
    width: 540px; height: 309px; position: relative; overflow: hidden;
    box-shadow: 0 10px 24px rgba(0,0,0,.45);
  }
  /* back */
  .card-back { background: var(--brand-deep); }
  .card-back .pattern {
    position: absolute; inset: 0;
    background: linear-gradient(135deg, var(--brand-navy) 0%, var(--brand-deep) 55%, #1379c0 100%);
  }
  .card-back .wordmark {
    position: absolute; left: 0; right: 0; top: 50%; transform: translateY(-50%);
    display: flex; align-items: center; justify-content: center; gap: 14px;
    font-family: "Montserrat", Arial, sans-serif; font-weight: 600;
    font-size: 48px; letter-spacing: 2px; color: var(--paper);
  }
  .mark-square { width: 34px; height: 34px; background: currentColor; display: block; }
  /* front */
  .card-front { background: var(--paper); }
  .card-front .faint-mark {
    position: absolute; right: 34px; top: 22px; width: 170px; height: 170px;
    border-radius: 22px; background: var(--faint);
  }
  .card-front .wordmark {
    position: absolute; left: 34px; top: 72px;
    display: flex; align-items: center; gap: 10px;
    font-family: "Montserrat", Arial, sans-serif; font-weight: 600;
    font-size: 34px; letter-spacing: 1px; color: var(--brand-blue);
  }
  .card-front .wordmark .mark-square { width: 24px; height: 24px; }
  .person { position: absolute; left: 54px; top: 134px; }
  .person-name {
    font-family: "Montserrat", Arial, sans-serif; font-weight: 700;
    font-size: 19px; line-height: 24px; color: var(--brand-blue);
  }
  .person-title { font-size: 13px; line-height: 16px; color: var(--ink-blue); }
  .contacts { list-style: none; margin-top: 8px; }
  .contacts li {
    display: flex; align-items: center; gap: 8px;
    font-size: 13px; color: var(--ink-blue); line-height: 19px;
  }
  .contacts svg { width: 12px; height: 12px; fill: var(--brand-blue); flex: none; }
  .contacts .icon-mail { fill: none; stroke: var(--brand-blue); stroke-width: 2.4; }
  .divider {
    position: absolute; left: 54px; right: 34px; top: 248px;
    height: 1px; background: var(--ink-blue);
  }
  .address {
    position: absolute; left: 54px; top: 256px;
    font-size: 12.5px; line-height: 16px; color: var(--ink-blue);
  }
  .bottom-band {
    position: absolute; left: 0; right: 0; bottom: 0; height: 8px;
    display: flex; gap: 4px;
  }
  .bottom-band .band-dark { width: 70px; background: var(--brand-navy); }
  .bottom-band .band-light { flex: 1; background: var(--brand-blue); }
</style>
</head>
<body>
  <section class="card card-back">
    <div class="pattern" role="img" aria-label="Repeating pattern of the company mark in shades of blue"></div>
    <div class="wordmark"><span class="mark-square"></span>KORVELLA</div>
  </section>

  <section class="card card-front">
    <div class="faint-mark" aria-hidden="true"></div>
    <div class="wordmark"><span class="mark-square"></span>KORVELLA</div>
    <div class="person">
      <p class="person-name">Daniel Marsh</p>
      <p class="person-title">Manager</p>
      <ul class="contacts">
        <li><svg viewBox="0 0 24 24"><path d="M6.6 10.8a15.1 15.1 0 0 0 6.6 6.6l2.2-2.2a1 1 0 0 1 1-.25 11.4 11.4 0 0 0 3.6.57 1 1 0 0 1 1 1V20a1 1 0 0 1-1 1A17 17 0 0 1 3 4a1 1 0 0 1 1-1h3.5a1 1 0 0 1 1 1c0 1.25.2 2.45.57 3.57a1 1 0 0 1-.25 1z"/></svg>555-014-2870</li>
        <li><svg class="icon-mail" viewBox="0 0 24 24"><path d="M2 5h20v14H2z M2 5l10 8 10-8"/></svg>contactus@korvellait.example</li>
        <li><svg viewBox="0 0 24 24"><circle cx="12" cy="12" r="10"/></svg>www.korvellait.example</li>
      </ul>
    </div>
    <div class="divider"></div>
    <p class="address">42 Linden Row, Suite 210, Brookfield, ST 00000</p>
    <div class="bottom-band"><span class="band-dark"></span><span class="band-light"></span></div>
  </section>
</body>
</html>
```